New CORPORATE WEBSITE DESIGN (Graphic layout for a WEBSITE TEMPLATE required - Photoshop files)

Hi – I need a draft created for a new corporate website for our company.
I need a graphic design concept which can be applied to a whole website layout -
I have a separate web development team who will implement the design onto Wordpress.
We are an Asian Buying Office based in Hong Kong and Shenzhen which facilitates relationships between factories in China and customers (retailers/etailers) all over the world.
We are a “boutique” agency, which offers highly customized services – we are highly consultative in our approach and tailor services to suit the needs of our customers with customized solutions. Our services are transparent partnership- and-integrity-based, and aimed to support at a certain size of company in growth mode.
We have dedicated teams of staff focused entirely on a customer’s business and we work TOGETHER with customers to solve their product design, patent, product engineering, goods production, quality control and supply chain challenges operating in 24/7 through our proprietary web-based supply chain platform called Cargoloom.
I have a PowerPoint which can be used to drive:
1) creative direction (colour palette etc) and to provide basic content for each “screen.” I would like to see design options based on the PowerPoint which offer creative ways to create a new look and feel for us for a corporate website which will not be social media enabled or ecommerce enabled. We do not put ANY customer brand names direct or references on our website – relationships are private. The home page of the website should say in the design style – “product design and branded global consumer goods” as well as “professional engineering and quality control proficiency”.
The website should be clean and functional – have the “usability” of the Pebble website but the “Meridian 300” look & feel of the Oran & Velt website (http://www.oranvelt-example.com/eng/global/home.php) – Oran & Velt is a benchmark for us. Oran & Velt is the largest company in our industry doing what we do.
I do not want to COPY this example - I am offering it as a benchmark for a CLEAN, vibrant, professional site which sends a good brand and services message. The target market is a global B to B market – SMEs who are well funded and growing, brands with growth potential, or large, established brands who are looking to a) build a supply chain partner to help them grow b) increase their revenues by managing their costs c) reduce their risk through an experience buyer’s agent such as ourselves – a partner with integrity who they can trust. The web site design must say “global consumer brands” WITHOUT DIRECTLY ALLUDING TO THE LOGOS AND/OR BRAND NAMES WE WORK WITH , " full service agency – managing the process from product design and engineering, quality control and risk management to product manufacturing and shipping logistics" and “accountability/integrity/transparency within the partnership.” Designer to choose colors to be used in the design - I have also attached my logo file to allow you to select a color palette which will be complementary.
PLEASE FEEL FREE TO ASK ANY QUESTIONS - I AM HAPPY TO PROVIDE MORE DETAILS.

```html
<!DOCTYPE html>
<html lang="en">
<head>
<meta charset="utf-8">
<title>Kestrel Harbor Limited</title>
<link href="https://fonts.googleapis.com/css2?family=Montserrat:ital,wght@0,300;0,400;0,500;0,600;0,700;1,400&display=swap" rel="stylesheet">
<style>
  :root {
    --navy: #0b2a5a;
    --navy-dark: #041c45;
    --ink: #222;
    --text: #555;
    --muted: #c4c6ca;
    --grey-icon: #a9a9a9;
    --social-blue: #3b5ba8;
    --panel: #f2f2f2;
    --footer: #4e4e50;
    --caption: rgba(118, 132, 153, 0.82);
    --button: #9ea3ab;
    --line: #d8d8d8;
  }
  * { box-sizing: border-box; margin: 0; padding: 0; }
  html, body { width: 1200px; height: 1140px; overflow: hidden; }
  body {
    position: relative;
    font-family: "Montserrat", sans-serif;
    color: var(--text);
    background: linear-gradient(#fff 0, #fff 140px, #f4f4f4 600px, #fff 1140px);
  }
  .page { position: absolute; left: 100px; top: 0; width: 1001px; height: 1140px; }
  .header {
    position: absolute; left: 0; top: 0; width: 1001px; height: 90px;
    background: #fff; border-left: 1px solid #e6e6e6; border-right: 1px solid #e6e6e6;
  }
  .brand { position: absolute; left: 16px; top: 16px; display: flex; align-items: center; gap: 12px; }
  .brand-mark { width: 54px; height: 54px; border-radius: 50%; background: var(--navy); }
  .brand-name { font-size: 21px; font-weight: 500; color: var(--navy); letter-spacing: .3px; }
  .social { position: absolute; right: 13px; top: 15px; display: flex; gap: 6px; }
  .social span { width: 21px; height: 21px; border-radius: 50%; background: var(--grey-icon); }
  .social span.active { background: var(--social-blue); }
  .search { position: absolute; left: 737px; top: 48px; width: 252px; height: 27px; display: flex; border: 1px solid #d6d6d6; }
  .search-btn { width: 26px; height: 25px; background: #d6d6d6; display: flex; align-items: center; justify-content: center; }
  .search-field { flex: 1; font-size: 12px; color: #aaa; padding: 6px 8px; }

  .nav {
    position: absolute; left: 0; top: 90px; width: 1200px; height: 50px;
    background: linear-gradient(180deg, var(--navy) 0%, var(--navy-dark) 100%);
  }
  .nav a {
    position: absolute; top: 19px; font-size: 12px; font-weight: 600; color: #fff;
    text-decoration: none; letter-spacing: .2px;
  }
  .nav .current::before {
    content: ""; position: absolute; left: -28px; top: -19px; width: 110px; height: 10px;
    background: radial-gradient(ellipse at top, rgba(160,190,230,.55), rgba(160,190,230,0) 70%);
  }

  .hero {
    position: absolute; left: 0; top: 140px; width: 1001px; height: 405px; overflow: hidden;
    background:
      radial-gradient(ellipse at 78% 45%, #e8d8d6 0%, rgba(232,216,214,0) 45%),
      radial-gradient(ellipse at 30% 55%, #dcc9c6 0%, rgba(220,201,198,0) 50%),
      linear-gradient(100deg, #d3d4d8 0%, #e6dcda 45%, #d9dbe0 100%);
  }
  .hero-title { position: absolute; left: 0; width: 100%; top: 78px; text-align: center; font-size: 50px; font-weight: 600; color: #646464; letter-spacing: .5px; }
  .hero-sub { position: absolute; left: 0; width: 100%; top: 147px; text-align: center; font-size: 19px; line-height: 24px; color: #666; font-weight: 400; }
  .hero-btn { position: absolute; left: 445px; top: 222px; width: 127px; height: 36px; background: var(--button); color: #fff; font-size: 14px; font-weight: 600; text-align: center; line-height: 36px; }
  .caption { position: absolute; left: 0; bottom: 0; width: 100%; height: 50px; background: var(--caption); }
  .caption p { position: absolute; left: 21px; top: 15px; color: #fff; font-style: italic; font-size: 16px; }
  .dots { position: absolute; right: 17px; top: 21px; display: flex; gap: 6px; }
  .dots span { width: 9px; height: 9px; border-radius: 50%; background: rgba(255,255,255,.5); }
  .dots span.on { background: #fff; }

  .steps { position: absolute; left: 0; top: 545px; width: 1001px; height: 212px; display: flex; background: var(--panel); }
  .step { position: relative; width: 250px; height: 212px; background: linear-gradient(180deg, #f7f7f7, #efefef); box-shadow: inset -2px 0 3px -2px rgba(0,0,0,.12); }
  .step-num { position: absolute; left: 19px; top: 33px; width: 28px; height: 28px; border-radius: 50%; background: var(--navy); color: #fff; font-size: 14px; font-weight: 700; text-align: center; line-height: 28px; }
  .step h3 { position: absolute; left: 52px; top: 36px; font-size: 18px; font-weight: 600; color: var(--ink); letter-spacing: .3px; }
  .step-arrow { position: absolute; left: 190px; top: 33px; }
  .step p { position: absolute; left: 20px; top: 80px; width: 215px; font-size: 12.3px; line-height: 16px; color: var(--text); }
  .more { font-size: 12px; font-weight: 700; color: var(--navy); letter-spacing: .4px; }
  .step .more { position: absolute; left: 21px; top: 174px; }

  .services { position: absolute; left: 0; top: 757px; width: 1001px; height: 323px; background: #fff; border: 1px solid #e4e4e4; }
  .services-head { position: absolute; left: 20px; top: 25px; font-size: 26px; font-weight: 700; color: var(--navy); letter-spacing: .5px; }
  .services-head span { font-size: 19px; font-weight: 500; color: var(--muted); letter-spacing: 0; margin-left: 6px; }
  .services-rule { position: absolute; left: 20px; top: 71px; width: 960px; height: 1px; background: var(--line); }
  .service { position: absolute; top: 100px; width: 310px; font-size: 12.3px; line-height: 16px; color: var(--text); }
  .service h4 { font-size: 16px; font-weight: 600; color: var(--ink); margin-bottom: 10px; letter-spacing: .3px; }
  .service ul { list-style: none; margin-top: 16px; }
  .service li::before { content: "• "; }
  .service .more { display: block; margin-top: 19px; margin-left: 1px; }

  .footer { position: absolute; left: 0; top: 1090px; width: 1001px; height: 50px; background: var(--footer); font-size: 12.5px; color: #cfcfcf; }
  .footer .copy { position: absolute; left: 21px; top: 18px; }
  .footer .links { position: absolute; right: 20px; top: 18px; }
  .footer strong { color: #fff; font-weight: 600; }
</style>
</head>
<body>
  <nav class="nav">
    <a style="left:150px">MENU 1</a>
    <a style="left:270px">MENU 2</a>
    <a class="current" style="left:390px">MENU 3</a>
    <a style="left:510px">MENU 4</a>
    <a style="left:640px">MENU 5</a>
    <a style="left:763px">MENU 6</a>
    <a style="left:879px">MENU 7</a>
    <a style="left:999px">MENU 8</a>
  </nav>

  <div class="page">
    <header class="header">
      <div class="brand">
        <div class="brand-mark"></div>
        <div class="brand-name">Kestrel Harbor Limited</div>
      </div>
      <div class="social"><span></span><span></span><span class="active"></span><span></span><span></span></div>
      <div class="search">
        <div class="search-btn">
          <svg width="12" height="12" viewBox="0 0 12 12"><circle cx="5" cy="5" r="3.5" fill="none" stroke="#fff" stroke-width="1.6"/><line x1="7.6" y1="7.6" x2="11" y2="11" stroke="#fff" stroke-width="1.8"/></svg>
        </div>
        <div class="search-field">Search...</div>
      </div>
    </header>

    <section class="hero" role="img" aria-label="Soft-focus fashion portrait photograph behind the headline">
      <h1 class="hero-title">Lorem Ipsum dolor</h1>
      <p class="hero-sub">Lorem ipsum dolor sit amet, consectetuer<br>adipiscing elit, sed diam nonummy nibh.</p>
      <div class="hero-btn">LEARN MORE</div>
      <div class="caption">
        <p>Lorem ipsum dolor sit amet, consectetuer adipiscing elit.</p>
        <div class="dots"><span class="on"></span><span></span><span></span><span></span></div>
      </div>
    </section>

    <section class="steps">
      <div class="step">
        <div class="step-num">1</div><h3>LOREM IPSUM</h3>
        <svg class="step-arrow" width="76" height="28" viewBox="0 0 76 28"><defs><linearGradient id="ar1" x1="0" x2="1"><stop offset="0" stop-color="#e6e6e6" stop-opacity="0"/><stop offset="1" stop-color="#d4d4d4"/></linearGradient></defs><path d="M0 8 H62 V0 L76 14 L62 28 V20 H0 Z" fill="url(#ar1)"/></svg>
        <p>Lorem ipsum dolor sit amet, consectetuer adipiscing elit, sed diam nonummy nibh euismod tincidunt ut laoreet dolore magna aliquam erat volutpat.</p>
        <span class="more">LEARN MORE</span>
      </div>
      <div class="step">
        <div class="step-num">2</div><h3>LOREM IPSUM</h3>
        <svg class="step-arrow" width="76" height="28" viewBox="0 0 76 28"><path d="M0 8 H62 V0 L76 14 L62 28 V20 H0 Z" fill="url(#ar1)"/></svg>
        <p>Lorem ipsum dolor sit amet, consectetuer adipiscing elit, sed diam nonummy nibh euismod tincidunt ut laoreet dolore magna aliquam erat volutpat.</p>
        <span class="more">LEARN MORE</span>
      </div>
      <div class="step">
        <div class="step-num">3</div><h3>LOREM IPSUM</h3>
        <svg class="step-arrow" width="76" height="28" viewBox="0 0 76 28"><path d="M0 8 H62 V0 L76 14 L62 28 V20 H0 Z" fill="url(#ar1)"/></svg>
        <p>Lorem ipsum dolor sit amet, consectetuer adipiscing elit, sed diam nonummy nibh euismod tincidunt ut laoreet dolore magna aliquam erat volutpat.</p>
        <span class="more">LEARN MORE</span>
      </div>
      <div class="step">
        <div class="step-num">4</div><h3>LOREM IPSUM</h3>
        <p>Lorem ipsum dolor sit amet, consectetuer adipiscing elit, sed diam nonummy nibh euismod tincidunt ut laoreet dolore magna aliquam erat volutpat.</p>
        <span class="more">LEARN MORE</span>
      </div>
    </section>

    <section class="services">
      <h2 class="services-head">SERVICES<span>What We Do</span></h2>
      <div class="services-rule"></div>
      <div class="service" style="left:20px">
        <h4>Service #1</h4>
        <p>Lorem ipsum dolor sit amet, consectetuer adipiscing elit, sed diam nonummy nibh:</p>
        <ul>
          <li>Duis autem vel eum iriure dolor in hendrerit in vulputate velit;</li>
          <li>Delenit augue duis dolore te feugait nulla;</li>
          <li>Investigationes demonstraverunt lectores legere;</li>
          <li>Dynamicus, qui sequitur mutationem consuetudium lectorum;</li>
        </ul>
        <span class="more">LEARN MORE</span>
      </div>
      <div class="service" style="left:346px">
        <h4 style="margin-left:3px">Service #2</h4>
        <p>Lorem ipsum dolor sit amet, consectetuer adipiscing elit, sed diam nonummy nibh:</p>
        <ul>
          <li>Duis autem vel eum iriure dolor in hendrerit in vulputate velit;</li>
          <li>Delenit augue duis dolore te feugait nulla;</li>
          <li>Investigationes demonstraverunt lectores legere;</li>
          <li>Dynamicus, qui sequitur mutationem consuetudium lectorum;</li>
        </ul>
        <span class="more" style="margin-left:2px">LEARN MORE</span>
      </div>
      <div class="service" style="left:674px">
        <h4>Service #3</h4>
        <p>Lorem ipsum dolor sit amet, consectetuer adipiscing elit, sed diam nonummy nibh:</p>
        <ul>
          <li>Duis autem vel eum iriure dolor in hendrerit in vulputate velit;</li>
          <li>Delenit augue duis dolore te feugait nulla;</li>
          <li>Investigationes demonstraverunt lectores legere;</li>
          <li>Dynamicus, qui sequitur mutationem consuetudium lectorum;</li>
        </ul>
        <span class="more">LEARN MORE</span>
      </div>
    </section>

    <footer class="footer">
      <p class="copy">© Copyright 2014 <strong>Kestrel Harbor Limited</strong>. All rights reserved.</p>
      <p class="links">About Us - <strong style="font-weight:500">User Agreement</strong> - Privacy Policy - Terms and Conditions</p>
    </footer>
  </div>
</body>
</html>
```